Corvane Industries business cards

We need business cards for our company Corvane Industries, based in Brisbane but trading world wide. We buy and sell Corvane Industries, generators and marine equipment. The design needs to be kept clean, simple but eye catching.
Please keep with our current logo (included) and further information can be included on request

Business

0792cd
33a6d7
85cae6
3276b5
0455a3
cedeed
cee9f5
ffffff

```html
<!DOCTYPE html>
<html lang="en">
<head>
<meta charset="utf-8">
<title>Corvane Industries Business Card</title>
<link href="https://fonts.googleapis.com/css2?family=Roboto:wght@300;500;700&family=Arimo:wght@400&display=swap" rel="stylesheet">
<style>
  :root {
    --page-bg: #d9dde1;
    --card-bg: #f2f5f7;
    --brand-navy: #1d4a72;
    --brand-square: #3276b5;
    --band-dark: #1b1f24;
    --band-light: #33a6d7;
    --band-mid: #0792cd;
    --band-deep: #0455a3;
    --band-text: #e4f2fa;
    --icon-tone: #cee9f5;
  }
  * { margin: 0; padding: 0; box-sizing: border-box; }
  html, body { width: 1200px; height: 970px; overflow: hidden; background: var(--page-bg); }
  .card {
    position: absolute; left: 50px; top: 180px; width: 1100px; height: 611px;
    background: linear-gradient(135deg, #f7f9fb, var(--card-bg) 60%, #e8edf1);
    box-shadow: 0 10px 30px rgba(0,0,0,0.15);
    overflow: hidden;
    font-family: "Arimo", Arial, sans-serif;
  }
  .brand-mark {
    position: absolute; left: 284px; top: 108px; width: 152px; height: 152px;
    border-radius: 14px; background: var(--brand-square);
  }
  .brand-name {
    position: absolute; left: 470px; top: 96px;
    font-family: "Roboto", Arial, sans-serif; font-weight: 700;
    font-size: 84px; line-height: 92px; color: var(--brand-navy);
  }
  .brand-suffix {
    position: absolute; right: 140px; top: 262px;
    font-family: "Roboto", Arial, sans-serif; font-weight: 700;
    font-size: 28px; color: var(--brand-navy);
  }
  .rule { position: absolute; left: 0; width: 100%; height: 14px; background: var(--band-dark); }
  .rule--top { top: 367px; }
  .rule--bottom { top: 543px; }
  .info-band {
    position: absolute; left: 0; top: 381px; width: 100%; height: 162px;
    background: linear-gradient(90deg, var(--band-light) 0%, var(--band-mid) 35%, var(--band-deep) 100%);
    color: var(--band-text);
  }
  .person { position: absolute; right: 779px; top: 48px; text-align: right; }
  .person-name { font-family: "Roboto", Arial, sans-serif; font-weight: 300; font-size: 36px; white-space: nowrap; }
  .person-role { font-size: 23px; letter-spacing: 4px; margin-top: 14px; margin-right: -4px; }
  .divider { position: absolute; left: 341px; top: 22px; width: 2px; height: 120px; background: var(--band-text); opacity: .8; }
  .contact { position: absolute; display: flex; align-items: center; font-size: 24px; white-space: nowrap; }
  .contact svg { width: 26px; height: 26px; margin-right: 14px; fill: var(--icon-tone); flex: none; }
  .contact--phone { left: 377px; top: 22px; }
  .contact--web { left: 377px; top: 58px; }
  .contact--mail { left: 377px; top: 96px; }
  .address { position: absolute; left: 768px; top: 22px; display: flex; font-size: 24px; line-height: 32px; }
  .address svg { width: 20px; height: 26px; margin: 3px 12px 0 0; fill: var(--icon-tone); flex: none; }
</style>
</head>
<body>
  <div class="card">
    <div class="brand-mark"></div>
    <div class="brand-name">Corvane<br>Industries</div>
    <div class="brand-suffix">Pty Ltd</div>

    <div class="rule rule--top"></div>
    <div class="info-band">
      <div class="person">
        <div class="person-name">Employee Name</div>
        <div class="person-role">Position</div>
      </div>
      <div class="divider"></div>

      <div class="contact contact--phone">
        <svg viewBox="0 0 24 24"><path d="M6.6 10.8a15.1 15.1 0 0 0 6.6 6.6l2.2-2.2c.3-.3.7-.4 1-.2 1.1.4 2.3.6 3.6.6.6 0 1 .4 1 1V20c0 .6-.4 1-1 1A17 17 0 0 1 3 4c0-.6.4-1 1-1h3.5c.6 0 1 .4 1 1 0 1.3.2 2.5.6 3.6.1.3 0 .7-.2 1z"/></svg>
        007-4821930
      </div>
      <div class="contact contact--web">
        <svg viewBox="0 0 24 24"><path d="M12 2a10 10 0 1 0 0 20 10 10 0 0 0 0-20zm6.9 6h-2.9a15.6 15.6 0 0 0-1.4-3.6A8 8 0 0 1 18.9 8zM12 4c.8 1.2 1.5 2.5 1.9 4h-3.8c.4-1.5 1.1-2.8 1.9-4zM4.3 14a8.2 8.2 0 0 1 0-4h3.4a16.5 16.5 0 0 0 0 4zm.8 2h2.9c.3 1.3.8 2.5 1.4 3.6A8 8 0 0 1 5.1 16zM8 8H5.1a8 8 0 0 1 4.3-3.6C8.8 5.5 8.3 6.7 8 8zm4 12c-.8-1.2-1.5-2.5-1.9-4h3.8c-.4 1.5-1.1 2.8-1.9 4zm2.3-6H9.7a14.7 14.7 0 0 1 0-4h4.6a14.7 14.7 0 0 1 0 4zm.3 5.6c.6-1.1 1.1-2.3 1.4-3.6h2.9a8 8 0 0 1-4.3 3.6zm1.7-5.6a16.5 16.5 0 0 0 0-4h3.4a8.2 8.2 0 0 1 0 4z"/></svg>
        www.corvaneindustries.com
      </div>
      <div class="contact contact--mail">
        <svg viewBox="0 0 24 24"><path d="M3 9l9-6 9 6v11a1 1 0 0 1-1 1H4a1 1 0 0 1-1-1zm2 1.2V19h14v-8.8l-7 4.6zM7 8v1.3l5 3.3 5-3.3V8z"/></svg>
        Yourname@corvaneindustries.com
      </div>

      <div class="address">
        <svg viewBox="0 0 20 26"><path d="M10 0a9 9 0 0 0-9 9c0 7 9 17 9 17s9-10 9-17a9 9 0 0 0-9-9zm0 12.5A3.5 3.5 0 1 1 10 5.5a3.5 3.5 0 0 1 0 7z"/></svg>
        <div>0142, Harlow Ave<br>Brisbane QLD 4000</div>
      </div>
    </div>
    <div class="rule rule--bottom"></div>
  </div>
</body>
</html>
```